Upmarket Bathroom and Kitchen ware supplier needs a classy business card design

We are a company based in Fiji, we sell plumbing ware (Kitchen and bathroom taps, Basins,showers, toilets etc) through up market show rooms to individuals and directly through Architects and designers of resorts and holiday houses for new builds and renovations. we are wanting to upgrade our over all look and brand. we are starting with a new logo but will be rebranding the whole business. This project is for a business card design for my management and tales team I would like it to be dark, classy and interesting

Target Market(s)

Resort directors and Management, High end holiday home owners

Contact Information for Business Card

Gavin Threlkeld
Director
+64219473518

Colors

Designer to choose colors to be used in the design.

Requirements
Must have
• Must have an upmarket appearance I like darker charcoal shades but will be guided by the designers
• Please any catch phrases like "Crafting remarkable living rooms" this belongs tpo one of our suppliers so can not be used.
Nice to have
• Double sided, so front dedicated to logo provided and back info about the business and the person.

```html
<!DOCTYPE html>
<html lang="en">
<head>
<meta charset="utf-8">
<title>Solace Interiors – Business Card</title>
<link rel="stylesheet" href="https://fonts.googleapis.com/css2?family=Montserrat:wght@300;400;600&display=swap">
<style>
  :root {
    --backdrop: #c9ccd1;
    --card: #3a3a3c;
    --card-deep: #323234;
    --ink: #ffffff;
    --ink-soft: #d9d9d9;
    --rule: #9a9a9a;
    --pattern-a: #353537;
    --pattern-b: #414143;
  }
  * { box-sizing: border-box; margin: 0; padding: 0; }
  html, body {
    width: 1200px; height: 900px; overflow: hidden;
    background: var(--backdrop);
    font-family: "Montserrat", sans-serif;
  }
  .stage {
    width: 1200px; height: 900px;
    display: flex; align-items: center; justify-content: center; gap: 80px;
  }
  .card {
    width: 340px; height: 520px;
    border-radius: 26px;
    background: var(--card);
    color: var(--ink);
    position: relative;
    overflow: hidden;
    box-shadow: 0 14px 30px rgba(0,0,0,0.25);
  }
  .card--front {
    display: flex; flex-direction: column; align-items: center;
    text-align: center;
    padding-top: 110px;
  }
  .brand__name {
    font-weight: 300; font-size: 30px; letter-spacing: 10px;
    padding-left: 10px;
    color: var(--ink);
  }
  .brand__rule {
    width: 170px; height: 1px; background: var(--rule);
    margin: 10px 0 8px;
  }
  .brand__sub {
    font-weight: 300; font-size: 10px; letter-spacing: 5px;
    padding-left: 5px; color: var(--ink);
  }
  .person { margin-top: 62px; }
  .person__name {
    font-weight: 600; font-size: 21px; letter-spacing: 0.5px;
    text-transform: uppercase;
  }
  .person__role {
    font-weight: 400; font-size: 13px; color: var(--ink-soft); margin-top: 4px;
  }
  .person__divider {
    width: 64px; height: 1px; background: var(--rule); margin: 18px auto 16px;
  }
  .address { font-size: 13px; line-height: 1.45; color: var(--ink-soft); }
  .contact-icons {
    display: flex; gap: 6px; justify-content: center; margin: 16px 0 12px;
  }
  .contact-icons svg { width: 10px; height: 10px; }
  .contact-list { font-size: 14px; line-height: 1.45; }
  .card--back {
    background: linear-gradient(135deg, var(--pattern-a), var(--card) 50%, var(--pattern-b));
    display: flex; align-items: center; justify-content: center;
  }
  .back__texture {
    position: absolute; inset: 0;
    background: linear-gradient(160deg, var(--card-deep) 0%, var(--pattern-b) 100%);
    opacity: 0.9;
  }
  .back__brand {
    position: relative;
    font-weight: 300; font-size: 22px; letter-spacing: 7px; padding-left: 7px;
    color: var(--ink);
  }
</style>
</head>
<body>
  <main class="stage">
    <section class="card card--front">
      <div class="brand">
        <div class="brand__name">SOLACE</div>
        <div class="brand__rule"></div>
        <div class="brand__sub">INTERIORS</div>
      </div>
      <div class="person">
        <div class="person__name">Gavin Threlkeld</div>
        <div class="person__role">Director</div>
        <div class="person__divider"></div>
        <div class="address">1742 Harbour View Lane<br>Lautoka Heights, Fiji</div>
        <div class="contact-icons">
          <svg viewBox="0 0 10 10" aria-label="phone"><path d="M2 1l2 0 .6 2-1.2 .8a5 5 0 0 0 2.8 2.8l.8-1.2 2 .6v2c0 .6-.4 1-1 1A8 8 0 0 1 1 2c0-.6.4-1 1-1z" fill="#fff"/></svg>
          <svg viewBox="0 0 10 10" aria-label="email"><rect x="1" y="2.5" width="8" height="5.5" fill="#fff"/><path d="M1 2.5l4 3 4-3" stroke="#3a3a3c" stroke-width="0.8" fill="none"/></svg>
          <svg viewBox="0 0 10 10" aria-label="website"><circle cx="5" cy="5" r="4" stroke="#fff" stroke-width="0.9" fill="none"/><ellipse cx="5" cy="5" rx="1.7" ry="4" stroke="#fff" stroke-width="0.7" fill="none"/><line x1="1" y1="5" x2="9" y2="5" stroke="#fff" stroke-width="0.7"/></svg>
        </div>
        <div class="contact-list">
          <div>+64219473518</div>
          <div>info@solaceware.com</div>
          <div>www.solaceware.com</div>
        </div>
      </div>
    </section>
    <section class="card card--back">
      <div class="back__texture" role="img" aria-label="Repeating tone-on-tone brand monogram pattern"></div>
      <div class="back__brand">SOLACE</div>
    </section>
  </main>
</body>
</html>
```